Larkspur Ridge Management - Business Cards

I need business cards. My current logo was designed by a designer at this site and I very much like and am happy with the results. I would like a business card that is trendy, unique, current yet professional. I deal with high net worth clients daily

Target Market(s)

Out of state investors looking to get into the rental market in Ohio

Industry/Entity Type

Property Management, Consulting

Contact Information for Business Card

Name, Title (Chief Financial Officer) office phone number (555) 817-3094 website address larkridgemgmt.example

Font styles to use
Sans Serif

Colors
0054AA
0677BA
7BADD7
CADEEF
E8F1F8
0094D4
00A9DD
6FCCEA
C7EBF8
E9F6FB
00AB8E
00BBA5
67D7C9
C6EFE9
E9F9F6

```html
<!DOCTYPE html>
<html lang="en">
<head>
<meta charset="utf-8">
<title>Larkspur Ridge Management – Business Cards</title>
<link href="https://fonts.googleapis.com/css2?family=Poppins:wght@400;500;700&display=swap" rel="stylesheet">
<style>
  :root {
    --board: #e2e2e2;
    --blue-core: #0054aa;
    --blue-mid: #00458f;
    --blue-edge: #002a5c;
    --strip: #00234d;
    --accent: #00bba5;
    --accent-deep: #00ab8e;
    --sky: #00a9dd;
    --sky-soft: #6fccea;
    --band-hi: #e9f6fb;
    --band-lo: #7badd7;
    --white: #ffffff;
    --rule: rgba(199,235,248,0.55);
    --icon-blue: #0677ba;
    --mark-bg: #003b7a;
  }
  * { margin: 0; padding: 0; box-sizing: border-box; }
  html, body { width: 944px; height: 1200px; overflow: hidden; }
  body {
    background: var(--board);
    font-family: "Poppins", sans-serif;
    color: var(--white);
    position: relative;
  }
  .card {
    position: absolute;
    left: 143px;
    width: 660px;
    height: 377px;
    overflow: hidden;
    background: radial-gradient(ellipse at 50% 45%, var(--blue-core) 0%, var(--blue-mid) 55%, var(--blue-edge) 100%);
    box-shadow: 0 6px 22px rgba(0,0,0,0.22);
  }
  .card--front { top: 138px; }
  .card--back { top: 659px; }

  /* front */
  .front-rule {
    position: absolute; left: 0; right: 0; top: 170px; height: 3px;
    background: var(--accent);
  }
  .brand {
    position: absolute;
    display: flex; align-items: center; gap: 12px;
    background: var(--mark-bg);
    padding: 18px 22px;
  }
  .brand__mark { width: 16px; height: 16px; background: var(--accent); flex: none; }
  .brand__name {
    font-weight: 700; font-size: 19px; line-height: 1.15;
    color: var(--white); letter-spacing: 0.5px; text-transform: uppercase;
  }
  .card--front .brand { left: 50%; top: 171px; transform: translate(-50%, -50%); }
  .silver-band {
    position: absolute; left: 0; right: 0; top: 297px; height: 8px;
    background: linear-gradient(90deg, var(--band-lo), var(--band-hi) 35%, #c7ebf8 60%, var(--band-hi) 80%, var(--band-lo));
  }
  .accent-tab {
    position: absolute; left: 169px; width: 321px; top: 303px; height: 14px;
    background: linear-gradient(180deg, var(--accent), var(--accent-deep));
    border-radius: 0 0 12px 12px;
  }
  .front-web {
    position: absolute; left: 0; right: 0; top: 331px;
    text-align: center; font-size: 15px; font-weight: 400;
  }
  .front-web b { font-weight: 700; }

  /* back */
  .side-strip {
    position: absolute; left: 0; top: 0; bottom: 0; width: 63px;
    background: var(--strip);
  }
  .side-silver {
    position: absolute; left: 63px; top: 0; bottom: 0; width: 4px;
    background: linear-gradient(90deg, var(--band-lo), var(--band-hi), var(--band-lo));
  }
  .side-tab {
    position: absolute; left: 67px; top: 96px; width: 8px; height: 184px;
    background: var(--accent); border-radius: 0 8px 8px 0;
  }
  .card--back .brand { left: 178px; top: 188px; transform: translate(-50%, -50%); }
  .person { position: absolute; left: 331px; top: 40px; }
  .person__name { font-size: 30px; line-height: 36px; font-weight: 500; letter-spacing: 0.3px; }
  .person__name strong { font-weight: 700; }
  .person__title { font-size: 21px; line-height: 28px; font-weight: 400; }
  .contact { position: absolute; left: 328px; top: 0; width: 300px; }
  .contact__row {
    position: absolute; left: 0; display: flex; align-items: center; gap: 16px;
    transform: translateY(-50%); white-space: nowrap;
  }
  .contact__icon { width: 38px; height: 42px; flex: none; }
  .contact__text { font-size: 16px; line-height: 20px; font-weight: 400; }
  .contact__rule { position: absolute; height: 1px; background: var(--rule); left: 49px; }
</style>
</head>
<body>

<section class="card card--front" aria-label="Card front">
  <div class="front-rule"></div>
  <div class="brand">
    <span class="brand__mark"></span>
    <span class="brand__name">Larkspur Ridge<br>Management</span>
  </div>
  <div class="silver-band"></div>
  <div class="accent-tab"></div>
  <p class="front-web">www.<b>larkridgemgmt</b>.example</p>
</section>

<section class="card card--back" aria-label="Card back">
  <div class="side-strip"></div>
  <div class="side-silver"></div>
  <div class="side-tab"></div>
  <div class="brand">
    <span class="brand__mark"></span>
    <span class="brand__name">Larkspur Ridge<br>Management</span>
  </div>

  <div class="person">
    <h1 class="person__name"><strong>CORRA</strong> VANTELL</h1>
    <p class="person__title">Chief Financial Officer</p>
  </div>

  <div class="contact">
    <div class="contact__row" style="top:152px">
      <svg class="contact__icon" viewBox="0 0 38 42" aria-hidden="true">
        <path d="M2 2h34v28L19 40 2 30z" fill="var(--icon-blue)" stroke="#fff" stroke-width="2"/>
        <path d="M13 11c1-1 2-1 3 0l2 3c0 1 0 2-1 2l-1 1c1 2 3 4 5 5l1-1c1-1 2-1 2 0l3 2c1 1 1 2 0 3l-1 1c-2 2-7 0-10-3s-5-8-3-10z" fill="#fff"/>
      </svg>
      <span class="contact__text">(555) 817-3094</span>
    </div>
    <div class="contact__rule" style="top:175px; width:236px"></div>

    <div class="contact__row" style="top:201px">
      <svg class="contact__icon" viewBox="0 0 38 42" aria-hidden="true">
        <path d="M2 2h34v28L19 40 2 30z" fill="var(--accent)" stroke="#fff" stroke-width="2"/>
        <rect x="10" y="12" width="18" height="13" fill="none" stroke="#fff" stroke-width="2"/>
        <path d="M10 12l9 7 9-7" fill="none" stroke="#fff" stroke-width="2"/>
      </svg>
      <span class="contact__text">hello@larkridgemgmt.example</span>
    </div>
    <div class="contact__rule" style="top:232px; width:255px"></div>

    <div class="contact__row" style="top:260px">
      <svg class="contact__icon" viewBox="0 0 38 42" aria-hidden="true">
        <path d="M2 2h34v28L19 40 2 30z" fill="var(--icon-blue)" stroke="#fff" stroke-width="2"/>
        <path d="M19 9a6 6 0 0 1 6 6c0 5-6 11-6 11s-6-6-6-11a6 6 0 0 1 6-6z" fill="#fff"/>
        <circle cx="19" cy="15" r="2.3" fill="var(--icon-blue)"/>
      </svg>
      <span class="contact__text">Orrin Plaza Suite 90,<br>Helena, MT 59601</span>
    </div>
    <div class="contact__rule" style="top:289px; width:236px"></div>

    <div class="contact__row" style="top:314px">
      <svg class="contact__icon" viewBox="0 0 38 42" aria-hidden="true">
        <path d="M2 2h34v28L19 40 2 30z" fill="var(--accent)" stroke="var(--sky-soft)" stroke-width="2"/>
        <circle cx="19" cy="18" r="8" fill="none" stroke="#fff" stroke-width="2"/>
        <path d="M11 18h16M19 10c-4 4-4 12 0 16M19 10c4 4 4 12 0 16" fill="none" stroke="#fff" stroke-width="1.6"/>
      </svg>
      <span class="contact__text">www.larkridgemgmt.example</span>
    </div>
  </div>
</section>

</body>
</html>
```